International sports trophy business needs a web design

We need two pages designed for a new company called medalnook. We sell innovative sports trophies via our website and store details of past purchases to allow returning customers to easily place their orders. Customers can log into their accounts using chatterlane or a secondary account login button. The final design should be clean and should focus on the theme of winning the trophy as it is applicable to all sports.

The page should be designed with themes that can be used throughout the site that we'll turn into a cms theme.
Updates

Hi All,

We're half way in to the competition now and I thought it'd be a good time to provide an update on how things are progressing.  First let me thank you for taking part, there's some really great ideas happening here however some of you have requested a mockup for the second page.  I've put that up now and you should be able to find it in the files section of the brief.  Hopefully this will give people a better starting point than before.

To everybody who is still waiting for feedback, be patient, I'm currently working my way through the designs and will be in contact shortly.  I thought in the meantime I could provide a general update as to how I think the competition is progressing and the concepts that I like the most so far. 

For the landing page... The designs that are leading at the moment are not busy or crowded and devote most of the page layout to the front page info-graphic.  The logo, login and primary menu are all easy to identify but not where your eye lands when viewing the page.  The copyright information and secondary menus are there if you look for them.  As far as the style goes we've found that some of the designs feel a little too serious and too adult and we'd like a more playful feel, if you think that your design already is playful, then we probably do too.  Finally I'll add that we like our logo, but that doesn't mean that we want to see it more than once on the landing page (it's pointless and designs that do this will be unlikely to win) and we certainly do not want to see people creating a new logo or changing our name to nook medal.

For the trophy sales page... There are fewer designs done to this specification as some are unwilling to invest the time in design or unwilling to work without a mockup.  The mockup has now been uploaded to the site (we did want to see what kind of ideas would come here if we didn't include one, thanks to those who had a shot).  If you have any other query about the sales page feel free to contact us.

A final general comment, we want to make sure that all of the images used in your designs are not infringing copyright (this includes images in our mockups, we can only guarantee that we own the copyright for the medalnook logo.).

Hi all, the sliders below have been updated to reflect the more playful design feel that we prefer so far.

Target Market(s)

Our target market is sporting and youth focused but must be adult friendly.

Industry/Entity Type

Business

Requirements
Must have
• We want two pages designed, a landing page and a product display page. We would like a common border scheme across both showing the logo (attached) in the top corner, and secondary links along the bottom.

Landing Page - Must Haves

We see trophies as a representation of achievement and something that can be shared with friends and family. We would like to convey this message in a graphic or illustration on the landing page. Currently in the mockup we have a bunch of trophies, this should not be the final image here.

We have attached a wireframe for the basic format that we'd like to see, you're free to expand upon this as you see fit.

Product Display Page - Must Haves

The product display page will feature a coverflow type device that holds images of the available trophies. It should show the category of the trophy, in this case choose a specific sport to feature (up to you). There should be space for the details of the trophy including price, dimensions, product name, product code, material. There should be room on the page for advertising, this will be common throughout the site except for the landing page. You should include buttons to allow you to add the trophy to your shopping cart and a shopping cart graphic somewhere on the page. There should be a menu bar, unique to this page, that allows a user to choose a new trophy to buy, view previous purchases, view current cart and account settings.

Should not have
• The design should be sport neutral, so don't focus on a single sport or category of sports or sports particular to a certain nationality. With that it's probably easier to just focus on the trophy and achievement aspect rather than the sport being played.

```html
<!DOCTYPE html>
<html lang="en">
<head>
<meta charset="utf-8">
<title>MedalNook – Landing</title>
<link rel="stylesheet" href="https://fonts.googleapis.com/css2?family=Source+Sans+3:ital,wght@0,400;0,600;1,400&family=PT+Sans:wght@400;700&display=swap">
<style>
  :root {
    --page-bg: #ffffff;
    --panel-border: #e3e3e3;
    --rule: #d6d6d6;
    --ink: #111111;
    --muted: #7a7a7a;
    --brand-red: #a0102e;
    --brand-red-dark: #6e0a1f;
    --brand-red-light: #d42a4c;
    --silver: #c9c9c9;
    --gold-light: #f3e4a0;
    --gold: #d8b440;
    --bronze: #d09070;
  }
  * { box-sizing: border-box; margin: 0; padding: 0; }
  html, body { width: 1200px; height: 633px; overflow: hidden; background: var(--page-bg); }
  body { position: relative; font-family: "PT Sans", Verdana, sans-serif; color: var(--ink); }

  .site-frame {
    position: absolute; left: 161px; top: 17px; width: 877px; height: 606px;
    border: 1px solid var(--panel-border); border-radius: 6px;
  }

  .site-mark {
    position: absolute; left: 553px; top: 34px; width: 94px; height: 94px;
    border-radius: 50%; background: var(--brand-red);
    display: flex; align-items: center; justify-content: center;
    color: #fff; font-family: "Source Sans 3", sans-serif; font-weight: 600; font-size: 15px;
  }

  .main-nav {
    position: absolute; left: 342px; top: 136px; width: 510px; height: 32px;
    border-top: 1px solid var(--rule); border-bottom: 1px solid var(--rule);
    display: flex; padding-left: 78px;
  }
  .main-nav a {
    display: block; height: 100%; line-height: 31px; color: var(--ink); text-decoration: none;
    font-family: "Source Sans 3", sans-serif; font-size: 20px; padding: 0 22px 0 7px;
  }
  .main-nav a + a { border-left: 1px solid var(--rule); padding-left: 24px; }

  .intro { position: absolute; left: 190px; top: 196px; width: 340px; text-align: center; }
  .intro-badge {
    width: 90px; height: 90px; border-radius: 50%; background: var(--brand-red);
    margin: 0 auto 12px;
  }
  .intro-name {
    font-family: "Source Sans 3", sans-serif; font-weight: 400; font-size: 38px;
    letter-spacing: 5px; color: var(--ink); line-height: 40px;
  }
  .intro-welcome {
    margin-top: 28px; font-family: "Source Sans 3", sans-serif; font-style: italic;
    font-size: 27px; line-height: 27px; color: var(--muted);
  }

  .auth-row { position: absolute; left: 195px; top: 452px; display: flex; align-items: center; }
  .btn {
    height: 32px; border-radius: 4px; color: #fff; text-decoration: none;
    background: linear-gradient(var(--brand-red-light), var(--brand-red) 55%, var(--brand-red-dark));
    display: flex; align-items: center;
  }
  .btn-login { width: 138px; font-family: "Source Sans 3", serif; font-size: 20px; }
  .btn-login svg { margin: 0 10px 0 4px; }
  .auth-or { font-size: 21px; font-family: "Source Sans 3", serif; margin: 0 9px 0 14px; }
  .btn-social { width: 156px; font-size: 11px; font-family: "Source Sans 3", serif; }
  .btn-social .square { width: 28px; height: 28px; background: #3a5a98; margin: 0 7px 0 2px; border-radius: 2px; }

  .join-note { position: absolute; left: 235px; top: 499px; font-size: 13px; color: var(--ink); }
  .join-note a { color: var(--ink); }

  .hero-graphic {
    position: absolute; left: 600px; top: 184px; width: 380px; height: 338px;
    background:
      linear-gradient(to bottom, rgba(255,255,255,0) 72%, #fff 100%),
      linear-gradient(90deg, #fff 2%, var(--silver) 18%, var(--gold-light) 40%, var(--gold) 52%, var(--gold-light) 64%, var(--bronze) 84%, #fff 98%);
    border-radius: 40px 40px 6px 6px; opacity: .85;
  }

  .site-footer {
    position: absolute; left: 132px; top: 584px; width: 935px;
    border-top: 2px solid #e8e8e8;
  }
  .copyright { position: absolute; left: 42px; top: 8px; font-size: 12px; font-weight: 700; }
  .secondary-nav { position: absolute; right: 47px; top: 7px; font-size: 12px; font-weight: 700; }
  .secondary-nav a { color: var(--ink); text-decoration: none; }
</style>
</head>
<body>
  <div class="site-frame"></div>

  <div class="site-mark">medalnook</div>

  <nav class="main-nav">
    <a href="#">Home</a><a href="#">What?</a><a href="#">Why?</a><a href="#">Tour</a>
  </nav>

  <section class="intro">
    <div class="intro-badge"></div>
    <h1 class="intro-name">MEDALNOOK</h1>
    <p class="intro-welcome">Welcome to Medal Nook, the newest online Trophy Store on the web.</p>
  </section>

  <div class="auth-row">
    <a class="btn btn-login" href="#">
      <svg width="40" height="28" viewBox="0 0 40 28"><path d="M2 8h20V1l16 13-16 13v-7H2z" fill="#8a8a8a" stroke="#555" stroke-width="1"/></svg>
      Login
    </a>
    <span class="auth-or">or</span>
    <a class="btn btn-social" href="#"><span class="square"></span>Connect with chatterlane</a>
  </div>

  <p class="join-note">Not a member yet? <a href="#">Click here to join</a></p>

  <div class="hero-graphic" role="img" aria-label="Silver, gold and bronze trophy cups standing side by side"></div>

  <footer class="site-footer">
    <span class="copyright">Copyright © 2011</span>
    <span class="secondary-nav"><a href="#">About</a> | <a href="#">Privacy policy</a> | <a href="#">Terms of Uses</a> | <a href="#">Help</a></span>
  </footer>
</body>
</html>
```